Business cards to launch an education platform

Hi,
I am looking at having new business cards designed.
I am a startup, developing a web platform for schools and university, the education world. It's an online assessment system.
I would like a card that looks classy, and that is using the colors and the font of my logo.

I have attached:
1) my logo
2) A business card that I have designed quickly so you can have all the information required in the card, but I really don't like it.
3) The font that I am using (Lato Regular) to design my web platform
4) Some screenshots of my web platform so you can have a look at the style that I have.

Target Market(s)

Major market: Education system: Schools and university
Minor markets: Business in general

Industry/Entity Type

Business

Contact Information for Business Card

Tessa Vinall
Director

M: 0487 312 950
E: tessa.vinall@copperLoomVentures.com.au

Requirements
Must have
• The colors of my logo

```html
<!DOCTYPE html>
<html lang="en">
<head>
<meta charset="utf-8">
<title>Copper Loom Ventures — Business Cards</title>
<link href="https://fonts.googleapis.com/css2?family=Lato:wght@400&display=swap" rel="stylesheet">
<style>
  :root {
    --backdrop: #e7e4e0;
    --card-navy: #1b3461;
    --text-light: #dbe7f4;
    --accent-sky: #3db3ea;
    --mark-blue: #2a7fd0;
    --card-shadow: rgba(20, 30, 50, 0.25);
  }
  * { box-sizing: border-box; margin: 0; padding: 0; }
  html, body {
    width: 1200px;
    height: 675px;
    overflow: hidden;
    background: var(--backdrop);
    font-family: "Lato", Arial, sans-serif;
  }
  .canvas {
    width: 1200px;
    height: 675px;
    display: flex;
    align-items: center;
    justify-content: center;
    gap: 44px;
  }
  .card {
    position: relative;
    width: 530px;
    height: 323px;
    background: var(--card-navy);
    box-shadow: 0 10px 28px var(--card-shadow);
    color: var(--text-light);
  }

  /* Front */
  .card-front {
    display: flex;
    flex-direction: column;
    align-items: center;
    justify-content: center;
  }
  .brand-square {
    width: 58px;
    height: 58px;
    background: var(--mark-blue);
    margin-bottom: 18px;
  }
  .brand-name {
    text-align: center;
    color: var(--text-light);
    font-weight: 400;
    line-height: 1.05;
  }
  .brand-name .line-main {
    display: block;
    font-size: 30px;
    letter-spacing: 3px;
    text-transform: uppercase;
  }
  .brand-name .line-sub {
    display: block;
    font-size: 24px;
    letter-spacing: 2.5px;
  }

  /* Back */
  .card-back .brand-name {
    position: absolute;
    top: 30px;
    left: 34px;
    text-align: left;
  }
  .card-back .brand-name .line-main { font-size: 26px; }
  .card-back .brand-name .line-sub { font-size: 21px; }

  .contact {
    position: absolute;
    left: 34px;
    bottom: 40px;
  }
  .person-name {
    font-size: 18px;
    color: var(--text-light);
  }
  .person-role {
    font-size: 12px;
    color: var(--accent-sky);
    margin-bottom: 18px;
  }
  .contact-list { list-style: none; }
  .contact-list li {
    display: flex;
    align-items: center;
    gap: 10px;
    font-size: 13px;
    line-height: 22px;
    color: var(--text-light);
  }
  .contact-icon {
    width: 12px;
    height: 12px;
    flex: none;
    stroke: var(--accent-sky);
    fill: none;
    stroke-width: 1.4;
  }
</style>
</head>
<body>
<main class="canvas">

  <section class="card card-front" aria-label="Card front">
    <div class="brand-square" aria-hidden="true"></div>
    <p class="brand-name">
      <span class="line-main">Copper Loom</span>
      <span class="line-sub">Ventures</span>
    </p>
  </section>

  <section class="card card-back" aria-label="Card back">
    <p class="brand-name">
      <span class="line-main">Copper Loom</span>
      <span class="line-sub">Ventures</span>
    </p>

    <div class="contact">
      <p class="person-name">Tessa Vinall</p>
      <p class="person-role">Director</p>
      <ul class="contact-list">
        <li>
          <svg class="contact-icon" viewBox="0 0 12 12" aria-hidden="true">
            <rect x="3" y="0.8" width="6" height="10.4" rx="1"/>
            <line x1="5" y1="9.4" x2="7" y2="9.4"/>
          </svg>
          0487 312 950
        </li>
        <li>
          <svg class="contact-icon" viewBox="0 0 12 12" aria-hidden="true">
            <rect x="0.8" y="2.3" width="10.4" height="7.4"/>
            <polyline points="0.8,2.3 6,6.6 11.2,2.3"/>
          </svg>
          tessa.vinall@copperLoomVentures.com.au
        </li>
        <li>
          <svg class="contact-icon" viewBox="0 0 12 12" aria-hidden="true">
            <circle cx="6" cy="6" r="5.2"/>
            <ellipse cx="6" cy="6" rx="2.2" ry="5.2"/>
            <line x1="0.8" y1="6" x2="11.2" y2="6"/>
          </svg>
          www.copperLoomVentures.com.au
        </li>
      </ul>
    </div>
  </section>

</main>
</body>
</html>
```